Website design for a Cloud Computing solution company

Name Liam
Title Head of marketing
Company Name 47Nimbo Networks Co., Ltd.
E-mail address liam.hou@47nimbo.example
Present URL (if any) www.47nimbo.example

Description of Project:

The web page style requirements: pages are clean, major color prefer light blue, white and black.
The current 4 Sketches as the page design reference.

What are the top three reasons why you currently have or want to build a Web site?

• Our products are mainly in the online sales.
• Easy to transfer our advantage and features of our product
• Built a communication platform based on cloud computing users to attract more users.

What are the target market that you would like to attract to your Web site and their demographics?

• Small and medium businesses .
• Personal webmaster.
• Startups Company via Internet.

What do you want a person to do once he or she comes to the site?
• Be interested in our product and click on child page to look up more information.
• Contacting with us on-line after browsing

LOOK AND FEEL: List example(s) of sites with a “look and feel” that you would like for your site.

https://www.fevrahost.example

SITE ORGANIZATION & LAYOUT: List one or two examples of sites with navigation and layout similar to the one you would like to develop.

https://www.fevrahost.example/

FEATURES: Please list all the features/facilities that you would like the website to provide your visitors. To help us understand better, please direct us to a sample site containing the feature.

1) We will use order pages templates and clinent management templates from PAYRIDGE.
2) All ICONs need to be redisigned and prefer to flat design.
3) Prefer to HTML5.
Is there any specific color scheme you want to follow or you like the most?

White and black overall and some light blue.

GRAPHICS: Do you have any graphics/logos/pictures that you would like us to use?

No.

If you have previously had a website, please indicate the features and ingredients that pleased you or displeased you.

No, we don't have existing website.

How can we look at that website?

www.tandrelhub.example (Not existing website)

Do you have an existing logo?
No

Industry/Entity Type

Marketing

```html
<!DOCTYPE html>
<html lang="en">
<head>
<meta charset="utf-8">
<title>Tandrel Hub — Cloud Hosting</title>
<link rel="stylesheet" href="https://fonts.googleapis.com/css2?family=Open+Sans:wght@400;600;700&display=swap">
<style>
:root{
  --blue:#0a78c8;
  --blue-dark:#0460a8;
  --blue-light:#1a9ae0;
  --green:#5cc43a;
  --nav-active:#7fe04a;
  --ink:#222;
  --grey-text:#666;
  --card-top:#f4f4f4;
  --card-bottom:#e4e4e4;
  --dark:#242424;
  --white:#fff;
}
*{box-sizing:border-box;margin:0;padding:0}
html,body{width:855px;height:1200px;overflow:hidden}
body{font-family:"Open Sans",Arial,sans-serif;background:var(--white);color:var(--ink);position:relative}
ul{list-style:none}

.site-header{position:absolute;left:0;top:0;width:855px;height:56px;background:linear-gradient(#0a86d6,#0566b4)}
.brand{position:absolute;left:72px;top:9px;font-size:28px;font-weight:700;color:var(--white);letter-spacing:.2px}
.main-nav{position:absolute;left:287px;top:20px;display:flex;gap:0}
.main-nav a{font-size:10px;font-weight:600;color:var(--white);text-decoration:none;margin-right:20px}
.main-nav a.active{color:var(--nav-active)}
.btn{position:absolute;top:16px;height:23px;font-size:10px;font-weight:600;color:var(--white);display:flex;align-items:center;justify-content:center;border-radius:2px}
.btn-register{left:674px;width:58px;background:#2b2b2b}
.btn-login{left:736px;width:48px;background:var(--green)}

.hero{position:absolute;left:0;top:56px;width:855px;height:368px;background:radial-gradient(ellipse at 55% 35%,#dff4ff 0%,#7cc8ef 14%,#2a86c4 34%,#0e4f86 62%,#08304f 100%)}
.hero-caption{position:absolute;left:70px;top:158px;width:242px;height:51px;background:rgba(20,60,70,.75);color:var(--white);font-size:16px;line-height:21px;padding:3px 7px}
.hero-dots{position:absolute;left:390px;top:338px;width:72px;height:18px;border-radius:9px;background:rgba(60,60,60,.7);display:flex;align-items:center;justify-content:center;gap:8px}
.hero-dots span{width:7px;height:7px;border-radius:50%;background:var(--white)}
.hero-dots span.on{background:transparent;border:1.5px solid var(--white)}

.cta-bar{position:absolute;left:0;top:424px;width:855px;height:50px;display:flex}
.cta{flex:none;height:50px;display:flex;align-items:center;justify-content:center;gap:12px;color:var(--white);font-size:19px;font-weight:700;letter-spacing:.3px}
.cta-trial{width:427px;background:linear-gradient(#6d6d6d,#3e3e3e)}
.cta-contact{width:428px;background:linear-gradient(#2e2e2e,#161616)}

.plans{position:absolute;left:86px;top:498px;display:flex;gap:8px}
.plan{width:223px;height:218px}
.plan-head{height:38px;background:linear-gradient(var(--blue-light),var(--blue-dark));color:var(--white);font-size:19px;font-weight:700;text-align:center;line-height:38px}
.plan-price{height:76px;background:var(--card-top);text-align:center;color:#777;padding-top:14px}
.plan-price p{font-size:17px;line-height:26px}
.plan-price small{font-size:12px}
.plan-features{height:104px;background:var(--card-bottom);text-align:center;font-size:9.5px;color:#444;padding-top:14px}
.plan-features li{line-height:19.2px}
.slide-arrow{position:absolute;top:594px}

.why{position:absolute;left:0;top:752px;width:855px;height:278px;background:radial-gradient(ellipse at 100% 0%,#a8c0a0 0%,#5d8a78 22%,#2f5a56 48%,#1a2f3a 75%,#15232d 100%)}
.why-title{position:absolute;top:36px;width:100%;text-align:center;color:var(--white);font-size:18px;font-weight:700}
.feature{position:absolute;width:230px;height:60px}
.feature-icon{position:absolute;left:0;top:0;width:54px;height:54px;border-radius:50%;background:#f2f2f2;display:flex;align-items:center;justify-content:center}
.feature h3{position:absolute;left:60px;top:1px;font-size:15.5px;font-weight:600;color:var(--white);white-space:nowrap}
.feature p{position:absolute;left:60px;top:24px;width:160px;font-size:8.5px;line-height:13.5px;color:#d8e0e0}

.site-footer{position:absolute;left:0;top:1030px;width:855px;height:122px}
.foot-col{position:absolute;top:30px}
.foot-col h4{font-size:12.5px;font-weight:400;color:#444;margin-bottom:10px}
.foot-col li{font-size:9.5px;color:#888;line-height:17.6px}
.foot-col li::before{content:"•";margin-right:5px;font-size:8px}
.foot-divider{position:absolute;left:595px;top:22px;width:1px;height:80px;background:#ccc}
.social{display:flex;gap:15px;margin-top:8px}
.social span{width:19px;height:19px;border-radius:2px}
.bottom-bar{position:absolute;left:0;top:1152px;width:855px;height:48px;background:var(--dark);color:#999;font-size:9.5px;text-align:center;line-height:48px;word-spacing:2px}
</style>
</head>
<body>

<header class="site-header">
  <div class="brand">Tandrel Hub</div>
  <nav class="main-nav">
    <a class="active">Home</a><a>Product</a><a>Control</a><a>Who's on Tandrel Hub</a><a>Help</a><a>Company</a>
  </nav>
  <div class="btn btn-register">REGISTER</div>
  <div class="btn btn-login">LOG IN</div>
</header>

<section class="hero" role="img" aria-label="Photo of a hand touching a glowing cloud shape over blue bokeh lights">
  <div class="hero-caption">Maecenas consequat semper doloreu posuere</div>
  <div class="hero-dots"><span class="on"></span><span></span><span></span><span></span></div>
</section>

<div class="cta-bar">
  <div class="cta cta-trial">
    <svg width="22" height="22" viewBox="0 0 22 22" fill="none" stroke="#fff" stroke-width="2"><path d="M13 3H3v16h16V9"/><path d="M9 13l1-4 9-8 3 3-9 8z" stroke-linejoin="round"/></svg>
    APPLY FOR TRIAL
  </div>
  <div class="cta cta-contact">
    <svg width="22" height="22" viewBox="0 0 24 24"><path fill="#fff" d="M5 2l4 1 1 5-3 2c1 3 4 6 7 7l2-3 5 1 1 4c0 2-2 3-4 3C9 21 3 15 2 6c0-2 1-4 3-4z"/></svg>
    CONTACT US
  </div>
</div>

<section class="plans">
  <article class="plan">
    <h2 class="plan-head">STANDARD</h2>
    <div class="plan-price"><p>XX $<small>/month</small></p><p>XXX $<small>/per year</small></p></div>
    <ul class="plan-features"><li>2.4GHZ 1CPU + 512M Memory</li><li>50G System Disk + 20G Data Disk</li><li>1 Public IP + 1M BGP (No Traffic Limited)</li><li>Multi OS Templates</li></ul>
  </article>
  <article class="plan">
    <h2 class="plan-head">ADVANCED</h2>
    <div class="plan-price"><p>XX $<small>/month</small></p><p>XXX $<small>/per year</small></p></div>
    <ul class="plan-features"><li>2.4GHZ 1CPU + 512M Memory</li><li>50G System Disk + 20G Data Disk</li><li>1 Public IP + 1M BGP (No Traffic Limited)</li><li>Multi OS Templates</li></ul>
  </article>
  <article class="plan">
    <h2 class="plan-head">LUXURIOUS</h2>
    <div class="plan-price"><p>XX $<small>/month</small></p><p>XXX $<small>/per year</small></p></div>
    <ul class="plan-features"><li>2.4GHZ 1CPU + 512M Memory</li><li>50G System Disk + 20G Data Disk</li><li>1 Public IP + 1M BGP (No Traffic Limited)</li><li>Multi OS Templates</li></ul>
  </article>
</section>
<svg class="slide-arrow" style="left:63px" width="14" height="24" viewBox="0 0 14 24"><path d="M12 2L3 12l9 10" fill="none" stroke="#aaa" stroke-width="2"/></svg>
<svg class="slide-arrow" style="left:778px" width="14" height="24" viewBox="0 0 14 24"><path d="M2 2l9 10-9 10" fill="none" stroke="#aaa" stroke-width="2"/></svg>

<section class="why">
  <h2 class="why-title">WHY US?</h2>

  <div class="feature" style="left:72px;top:84px">
    <div class="feature-icon"><svg width="18" height="20" viewBox="0 0 18 20"><path d="M9 1l8 3v6c0 5-4 8-8 9-4-1-8-4-8-9V4z" fill="#222"/></svg></div>
    <h3>Stringent Security</h3>
    <p>Pellentesque habitant morbi tristique senectus et netus et male suada fames ac turpis egestas.</p>
  </div>
  <div class="feature" style="left:330px;top:84px">
    <div class="feature-icon"><svg width="20" height="20" viewBox="0 0 20 20" fill="none" stroke="#222" stroke-width="2"><rect x="2" y="2" width="16" height="16"/><path d="M2 7h16M2 12h16M11 4.5h5M11 9.5h5M11 14.5h5" stroke-width="1.5"/></svg></div>
    <h3>Distributed Storage</h3>
    <p>Pellentesque habitant morbi tristique senectus et netus et male suada fames ac turpis egestas.</p>
  </div>
  <div class="feature" style="left:567px;top:84px">
    <div class="feature-icon"><svg width="24" height="22" viewBox="0 0 24 22" fill="none" stroke="#222" stroke-width="2"><rect x="2" y="2" width="20" height="14"/><path d="M12 16v4M7 20h10"/><path d="M5 9h4l2-3 2 6 2-3h4" stroke-width="1.3"/></svg></div>
    <h3>Exceptional Reliability</h3>
    <p>Pellentesque habitant morbi tristique senectus et netus et male suada fames ac turpis egestas.</p>
  </div>
  <div class="feature" style="left:72px;top:181px">
    <div class="feature-icon"><svg width="22" height="22" viewBox="0 0 22 22"><circle cx="11" cy="11" r="9.5" fill="#222"/><path d="M6 5c2 1 3 3 2 5-2 0-3 2-2 4M13 3c-1 2 1 3 3 3 1 2 0 4-2 5 0 2 1 4 3 4" fill="none" stroke="#f2f2f2" stroke-width="1.6"/></svg></div>
    <h3>High Quality Network</h3>
    <p>Pellentesque habitant morbi tristique senectus et netus et male suada fames ac turpis egestas.</p>
  </div>
  <div class="feature" style="left:330px;top:181px">
    <div class="feature-icon"><svg width="24" height="24" viewBox="0 0 24 24" fill="none" stroke="#222" stroke-width="2.4" stroke-linecap="round"><path d="M4 20L15 9"/><path d="M15 9a4 4 0 1 0 0-1"/><path d="M5 4l15 16"/><path d="M3 6l3-3"/></svg></div>
    <h3>Short time to Setup</h3>
    <p>Pellentesque habitant morbi tristique senectus et netus et male suada fames ac turpis egestas.</p>
  </div>
  <div class="feature" style="left:567px;top:181px">
    <div class="feature-icon"><svg width="22" height="22" viewBox="0 0 22 22"><circle cx="11" cy="11" r="9.5" fill="#222"/><circle cx="11" cy="11" r="7.5" fill="none" stroke="#f2f2f2" stroke-width=".8"/><path d="M11 6v5h4" fill="none" stroke="#f2f2f2" stroke-width="1.6"/></svg></div>
    <h3>24/7 Monitoring</h3>
    <p>Pellentesque habitant morbi tristique senectus et netus et male suada fames ac turpis egestas.</p>
  </div>
</section>

<footer class="site-footer">
  <div class="foot-col" style="left:110px"><h4>Help</h4><ul><li>Guidelin</li><li>FAQ</li><li>ICP</li></ul></div>
  <div class="foot-col" style="left:198px"><h4>Company</h4><ul><li>About us</li><li>News</li><li>Join</li></ul></div>
  <div class="foot-col" style="left:300px"><h4>Customers</h4><ul><li>Game</li><li>Finance</li><li>Others</li></ul></div>
  <div class="foot-col" style="left:400px"><h4>Support</h4><ul><li>Contact us</li><li>On-line Services</li></ul></div>
  <div class="foot-col" style="left:519px"><h4>Call us</h4><ul><li>400&nbsp; xxx&nbsp; xxxx</li></ul></div>
  <div class="foot-divider"></div>
  <div class="foot-col" style="left:651px">
    <h4>Connect with us</h4>
    <div class="social"><span style="background:#3b5998"></span><span style="background:#33b5e5"></span><span style="background:#333"></span></div>
  </div>
</footer>
<div class="bottom-bar">Copyright © 2014 Tandrel Hub &nbsp;All rights reserved.</div>

</body>
</html>
```